Sunny Doodles - Face Painting Company requires business card design

Hi,
I am wanting a business card design for a new business in Brisbane (Australia) called 'Sunny Doodles'. We are a childrens face painting company.

I want to communicate a corporate, simple and clean message through my business card, but also fun and relevant to children.

My company colours are black, yellow and purple, and at the moment I am running with a "cheeky smile" type theme, along the lines of the Marlow Fox (Tobin and the Glass Kite).

I want this to look Corporate, clean and simple. On the back I would like to see some creative flair with a border or background design, perhaps in white or another colour.

• Front:
Sunny Doodles
Face Painting Designs

Back:
Hana Melrose
Artist
0432 918 246
hana@sunnydoodles.com.au
www.sunnydoodles.com.au
• Attached is the banner which i had made, the business card should go along with this type of theme.
I would like to use the colours Yellow, Black and Purple. Purple should be used in a miniml way, with yellow and black as the main colours.
I want it to have a CORPORATE look.

A Playfull but readable text.

I would like a mix up of the colours on the back in the text.
Hana Melrose (black)
Artist(purple) etc.

```html
<!DOCTYPE html>
<html lang="en">
<head>
<meta charset="utf-8">
<title>Sunny Doodles – Business Card</title>
<link rel="stylesheet" href="https://fonts.googleapis.com/css2?family=Quicksand:wght@400;500;700&display=swap">
<style>
  :root {
    --page: #ffffff;
    --card-frame: #e3e3e3;
    --sunny-yellow: #f0fc12;
    --ink: #000000;
    --grape: #8c12ea;
    --tooth-white: #ffffff;
  }
  * { box-sizing: border-box; margin: 0; padding: 0; }
  html, body {
    width: 920px; height: 1200px; overflow: hidden;
    background: var(--page);
    font-family: "Quicksand", sans-serif;
  }
  .sheet { position: relative; width: 920px; height: 1200px; }
  .card-frame {
    position: absolute; left: 29px; width: 860px;
    background: var(--card-frame);
  }
  .card-frame--back { top: 54px; height: 541px; }
  .card-frame--front { top: 607px; height: 541px; }
  .card {
    position: absolute; left: 16px; top: 14px;
    width: 829px; height: 510px;
    background: var(--sunny-yellow);
    overflow: hidden;
  }
  .card-frame--front .card { top: 15px; }

  .grin-area {
    position: absolute;
    background: linear-gradient(135deg, var(--ink) 0%, #3a3a3a 45%, var(--tooth-white) 100%);
    opacity: 0.9;
  }
  .card-frame--back .grin-area {
    left: 0; top: 242px; width: 415px; height: 225px;
    border-radius: 0 60% 40% 0 / 0 20% 80% 0;
  }
  .card-frame--front .grin-area {
    left: 421px; top: 108px; width: 408px; height: 368px;
    border-radius: 30% 0 0 70% / 20% 0 0 80%;
  }

  .contact {
    position: absolute; right: 46px; top: 50px;
    text-align: right; font-weight: 500; line-height: 1;
  }
  .contact__name { font-size: 46px; color: var(--grape); font-weight: 400; }
  .contact__role { font-size: 46px; color: var(--grape); font-weight: 400; margin-top: 14px; }
  .contact__phone { font-size: 37px; color: var(--ink); margin-top: 104px; }
  .contact__email, .contact__web { font-size: 32px; color: var(--ink); margin-top: 10px; }
  .contact__email { margin-top: 8px; }
  .contact__abn { font-size: 17px; color: var(--ink); margin-top: 36px; }

  .brand {
    position: absolute; left: 24px; top: 230px; width: 370px;
    text-align: center;
  }
  .brand__name {
    font-size: 40px; font-weight: 700; color: var(--ink);
    text-transform: uppercase; letter-spacing: 1px; line-height: 1;
  }
  .brand__tagline {
    font-size: 17px; font-weight: 700; color: var(--grape);
    text-transform: uppercase; letter-spacing: 1px; margin-top: 8px;
  }
</style>
</head>
<body>
  <main class="sheet">
    <section class="card-frame card-frame--back">
      <div class="card">
        <div class="grin-area" role="img" aria-label="Illustration of a wide cheeky grin with white teeth outlined in black"></div>
        <div class="contact">
          <p class="contact__name">Hana Melrose</p>
          <p class="contact__role">Artist</p>
          <p class="contact__phone">0432 918 246</p>
          <p class="contact__email">hana@sunnydoodles.com.au</p>
          <p class="contact__web">www.sunnydoodles.com.au</p>
          <p class="contact__abn">ABN 5230714869</p>
        </div>
      </div>
    </section>

    <section class="card-frame card-frame--front">
      <div class="card">
        <div class="brand">
          <p class="brand__name">Sunny Doodles</p>
          <p class="brand__tagline">Face Painting Designs</p>
        </div>
        <div class="grin-area" role="img" aria-label="Illustration of a curling cheeky grin with white teeth outlined in black"></div>
      </div>
    </section>
  </main>
</body>
</html>
```